Valmin & Co Powerpoint Template

A simple powerpoint template for my business which provides management consulting services for Business Owners.

It should reflect the colours within the logo design and should work as the master template for all standard powerpoint slide layouts.

```html
<!DOCTYPE html>
<html lang="en">
<head>
<meta charset="utf-8">
<title>Valmin &amp; Co — Presentation Template</title>
<link href="https://fonts.googleapis.com/css2?family=Marcellus&family=Montserrat:wght@400;500&family=Open+Sans:wght@400;600;700;800&display=swap" rel="stylesheet">
<style>
  :root {
    --ink: #000000;
    --charcoal: #1c1c1c;
    --orange: #e05e20;
    --white: #ffffff;
    --muted: #b9b9b9;
    --frame-line: #e07a2e;
  }
  * { box-sizing: border-box; margin: 0; padding: 0; }
  html, body { width: 1200px; height: 4158px; overflow: hidden; background: var(--white); }
  body { position: relative; font-family: "Open Sans", Arial, sans-serif; color: var(--white); }

  .slide { position: absolute; left: 24px; width: 1153px; height: 650px; background: var(--ink); overflow: hidden; }
  .slide > * { position: absolute; }

  .photo { display: block; }

  /* small brand mark, top right */
  .brand-mark { left: 1001px; top: 19px; width: 140px; height: 80px; }
  .brand-mark .dot { position: absolute; left: 0; top: 6px; width: 36px; height: 36px; border-radius: 50%; background: var(--orange); }
  .brand-mark .name { position: absolute; left: 66px; top: 0; font-family: "Marcellus", Georgia, serif; font-size: 19px; line-height: 20px; color: var(--white); }
  .brand-mark .tag { position: absolute; left: 0; top: 66px; font-family: "Montserrat", Arial, sans-serif; font-size: 8.5px; color: var(--muted); white-space: nowrap; }

  .heading { font-weight: 700; font-size: 46px; line-height: 64px; color: var(--white); }
  .body-copy { font-size: 12px; line-height: 24px; color: var(--white); }
  .body-copy.strong { font-weight: 600; }

  /* cover */
  .cover { top: 24px; height: 649px; background: radial-gradient(ellipse at 55% 45%, #2e2b29 0%, #1a1918 60%, #0f0f0f 100%); }
  .cover .emblem { left: 250px; top: 170px; width: 170px; height: 170px; border-radius: 50%; background: var(--orange); }
  .cover .divider { left: 508px; top: 113px; width: 5px; height: 348px; background: var(--white); }
  .cover .wordmark { left: 582px; top: 128px; font-family: "Marcellus", Georgia, serif; font-size: 92px; line-height: 105px; color: var(--white); }
  .cover .tagline { left: 0; width: 1153px; top: 486px; text-align: center; font-family: "Montserrat", Arial, sans-serif; font-size: 44px; letter-spacing: 2px; color: var(--white); }

  /* history */
  .history { top: 713px; }
  .history .band { left: 551px; top: 0; width: 354px; height: 650px; background: var(--orange); }
  .history .photo { left: 629px; top: 115px; width: 417px; height: 454px; background: linear-gradient(160deg, #5b86a8 0%, #8a6a4c 45%, #a4734a 70%, #4d6f8a 100%); }
  .history .heading { left: 45px; top: 96px; }
  .history .body-copy { left: 45px; top: 252px; width: 470px; }

  /* services */
  .services { top: 1400px; }
  .services .frame { left: 16px; top: 23px; width: 429px; height: 404px; border: 2px solid var(--frame-line); }
  .services .p1 { left: 31px; top: 36px; width: 268px; height: 241px; background: linear-gradient(150deg, #c9ccce, #8b7e72 60%, #c65f24); }
  .services .p2 { left: 327px; top: 36px; width: 268px; height: 323px; background: linear-gradient(160deg, #c3c8cc, #3c4252 60%, #9aa2ad); }
  .services .p3 { left: 31px; top: 293px; width: 268px; height: 323px; background: linear-gradient(140deg, #dfe2e6, #3a3c40 50%, #c44e4a 80%, #e6e6e6); }
  .services .p4 { left: 327px; top: 375px; width: 268px; height: 241px; background: linear-gradient(160deg, #e8ebee, #a88f7d 55%, #55616d); }
  .services .heading { left: 640px; top: 96px; }
  .services .copy-a { left: 640px; top: 250px; width: 460px; }
  .services .copy-b { left: 640px; top: 468px; width: 460px; }

  /* business plan */
  .plan { top: 2088px; }
  .plan .heading { left: 31px; top: 28px; }
  .plan .intro { left: 377px; top: 26px; width: 560px; }
  .plan .column { top: 168px; width: 348px; }
  .plan .column .photo { width: 348px; height: 236px; }
  .plan .column h3 { margin-top: 32px; text-align: center; font-size: 22px; font-weight: 700; line-height: 30px; }
  .plan .column p { margin-top: 8px; text-align: center; font-size: 11px; line-height: 24px; font-weight: 600; }
  .plan .c1 { left: 32px; } .plan .c2 { left: 404px; } .plan .c3 { left: 776px; }
  .plan .c1 .photo { background: linear-gradient(150deg, #e4e6e8, #6e6a66 55%, #c9cbce); }
  .plan .c2 .photo { background: linear-gradient(160deg, #dfe3e6, #454b56 55%, #b7bcc2); }
  .plan .c3 .photo { background: linear-gradient(150deg, #eef0f2, #b7a595 55%, #7c8793); }

  /* value */
  .value { top: 2777px; }
  .value .v1 { left: 29px; top: 32px; width: 346px; height: 280px; background: linear-gradient(150deg, #e9ecee, #8b99a8 55%, #c9ced2); }
  .value .v2 { left: 29px; top: 344px; width: 346px; height: 279px; background: linear-gradient(150deg, #e7e3dc, #6f6a62 50%, #c46b2e 80%, #dcdcdc); }
  .value .heading { left: 433px; top: 54px; }
  .value .copy-a { left: 438px; top: 210px; width: 575px; }
  .value .copy-b { left: 438px; top: 420px; width: 575px; }
  .value .body-copy { line-height: 24px; }

  /* closing */
  .closing { top: 3466px; }
  .closing .emblem { left: 125px; top: 190px; width: 260px; height: 260px; border-radius: 50%; background: var(--orange); }
  .closing .thanks { left: 538px; top: 84px; font-size: 46px; font-weight: 800; color: var(--orange); }
  .closing .wordmark { left: 538px; top: 166px; font-size: 72px; font-weight: 800; color: var(--orange); line-height: 100px; }
  .closing .tagline { left: 538px; top: 278px; font-size: 32px; color: var(--white); }
  .closing .body-copy { left: 538px; top: 356px; width: 575px; font-size: 12.5px; line-height: 22px; }
  .closing .social { top: 478px; width: 28px; height: 28px; border-radius: 50%; background: var(--orange); }
  .closing .s1 { left: 540px; } .closing .s2 { left: 598px; } .closing .s3 { left: 656px; }
</style>
</head>
<body>

<section class="slide cover">
  <div class="emblem" aria-hidden="true"></div>
  <div class="divider"></div>
  <div class="wordmark">Valmin<br>&amp;<br>Co</div>
  <div class="tagline">Supporting Business Owners</div>
</section>

<section class="slide history">
  <div class="band"></div>
  <div class="photo" role="img" aria-label="Team meeting around a wooden table seen from above, two colleagues shaking hands"></div>
  <div class="brand-mark"><span class="dot"></span><span class="name">Valmin<br>&amp;<br>Co</span><span class="tag">Supporting Business Owners</span></div>
  <h2 class="heading">Our<br>History</h2>
  <p class="body-copy">Sed ut perspiciatis unde omnis iste natus error sit voluptatem accusantium doloremque laudantium, totam rem aperiam, eaque ipsa quae ab illo inventore veritatis et quasi architecto beatae vitae dicta sunt explicabo. Nemo enim ipsam voluptatem quia voluptas sit aspernatur aut odit aut fugit, sed quia consequuntur magni dolores eos qui ratione voluptatem sequi nesciunt. Neque porro quisquam est, qui dolorem ipsum quia dolor sit amet, consectetur, adipisci velit, sed quia non numquam eius modi tempora incidunt ut labore et dolore magnam aliquam quaerat voluptatem. Sed ut perspiciatis unde omnis iste natus error sit voluptatem accusantium doloremque laudantium, totam rem aperiam, eaque ipsa quae ab illo inventore veritatis et quasi architecto beatae vitae dicta sunt explicabo. Nemo enim ipsam voluptatem quia voluptas sit aspernatur aut odit aut fugit, sed quia consequuntur magni dolores eos qui</p>
</section>

<section class="slide services">
  <div class="frame"></div>
  <div class="photo p1" role="img" aria-label="Consultant presenting at a whiteboard to a colleague"></div>
  <div class="photo p2" role="img" aria-label="Three colleagues reviewing documents at a desk"></div>
  <div class="photo p3" role="img" aria-label="Tablet showing business charts on a desk"></div>
  <div class="photo p4" role="img" aria-label="Support staff wearing headsets"></div>
  <div class="brand-mark"><span class="dot"></span><span class="name">Valmin<br>&amp;<br>Co</span><span class="tag">Supporting Business Owners</span></div>
  <h2 class="heading">Our<br>Services</h2>
  <p class="body-copy strong copy-a">Sed ut perspiciatis unde omnis iste natus error sit voluptatem accusantium doloremque laudantium, totam rem aperiam, eaque ipsa quae ab illo inventore veritatis et quasi architecto beatae vitae dicta sunt explicabo. Nemo enim ipsam voluptatem quia voluptas sit aspernatur aut odit aut fugit, sed quia consequuntur magni dolores eos qui ratione voluptatem sequi nesciunt. Neque porro quisquam est, qui dolorem ipsum quia dolor sit amet, consectetur, adipisci velit, sed quia non numquam eius modi tempora incidunt ut labore et dolore magnam aliquam quaerat voluptatem.</p>
  <p class="body-copy copy-b">Sed ut perspiciatis unde omnis iste natus error sit voluptatem accusantium doloremque laudantium, totam rem aperiam, eaque ipsa quae ab illo inventore veritatis et quasi architecto beatae vitae dicta sunt explicabo. Nemo enim ipsam voluptatem quia voluptas sit aspernatur aut odit aut fugit, sed quia consequuntur magni dolores eos qui ratione voluptatem sequi nesciunt. Neque porro quisquam est, qui dolorem ipsum quia dolor sit amet, consectetur,</p>
</section>

<section class="slide plan">
  <h2 class="heading">Business Plan</h2>
  <p class="body-copy strong intro">Sed ut perspiciatis unde omnis iste natus error sit voluptatem accusantium doloremque laudantium, totam rem aperiam, eaque ipsa quae ab illo inventore veritatis et quasi architecto beatae vitae dicta sunt explicabo.</p>
  <div class="brand-mark"><span class="dot"></span><span class="name">Valmin<br>&amp;<br>Co</span><span class="tag">Supporting Business Owners</span></div>
  <div class="column c1">
    <div class="photo" role="img" aria-label="Team discussion around a meeting table"></div>
    <h3>Nemo enim ipsam</h3>
    <p>Sed ut perspiciatis unde omnis iste natus error sit voluptatem accusantium doloremque laudantium, totam rem aperiam, eaque ipsa quae.</p>
  </div>
  <div class="column c2">
    <div class="photo" role="img" aria-label="Two colleagues working together at a computer"></div>
    <h3>Nemo enim ipsam</h3>
    <p>Sed ut perspiciatis unde omnis iste natus error sit voluptatem accusantium doloremque laudantium, totam rem aperiam, eaque ipsa quae.</p>
  </div>
  <div class="column c3">
    <div class="photo" role="img" aria-label="Presenter at a whiteboard addressing a small group"></div>
    <h3>Nemo enim ipsam</h3>
    <p>Sed ut perspiciatis unde omnis iste natus error sit voluptatem accusantium doloremque laudantium, totam rem aperiam, eaque ipsa quae.</p>
  </div>
</section>

<section class="slide value">
  <div class="photo v1" role="img" aria-label="Consultant on a phone call at his desk"></div>
  <div class="photo v2" role="img" aria-label="Colleagues planning with sticky notes on a glass wall"></div>
  <div class="brand-mark"><span class="dot"></span><span class="name">Valmin<br>&amp;<br>Co</span><span class="tag">Supporting Business Owners</span></div>
  <h2 class="heading">Our<br>Value</h2>
  <p class="body-copy strong copy-a">Sed ut perspiciatis unde omnis iste natus error sit voluptatem accusantium doloremque laudantium, totam rem aperiam, eaque ipsa quae ab illo inventore veritatis et quasi architecto beatae vitae dicta sunt explicabo. Sed ut perspiciatis unde omnis iste natus error sit voluptatem accusantium doloremque laudantium, totam rem aperiam, eaque ipsa quae ab illo inventore veritatis et quasi architecto beatae vitae dicta sunt explicabo. Sed ut perspiciatis unde omnis iste natus error sit voluptatem accusantium doloremque laudantium, totam rem aperiam, eaque ipsa quae ab illo inventore veritatis et quasi architecto beatae vitae dicta sunt explicabo.</p>
  <p class="body-copy strong copy-b">Sed ut perspiciatis unde omnis iste natus error sit voluptatem accusantium doloremque laudantium, totam rem aperiam, eaque ipsa quae ab illo inventore veritatis et quasi architecto beatae vitae dicta sunt explicabo. Sed ut perspiciatis unde omnis iste natus error sit voluptatem accusantium doloremque laudantium, totam rem aperiam, eaque ipsa quae ab illo inventore veritatis et quasi architecto beatae vitae dicta sunt explicabo. Sed ut perspiciatis unde omnis iste natus error sit voluptatem accusantium doloremque laudantium, totam rem aperiam, eaque ipsa quae ab illo inventore veritatis et quasi architecto beatae vitae dicta sunt explicabo.</p>
</section>

<section class="slide closing">
  <div class="emblem" aria-hidden="true"></div>
  <h2 class="thanks">Thank You</h2>
  <div class="wordmark">Valmin&amp;co</div>
  <div class="tagline">Supporting Business Owners</div>
  <p class="body-copy">Lorem ipsum dolor sit amet, consectetur adipiscing elit, sed do eiusmod tempor incididunt ut labore et dolore magna aliqua. Ut enim ad minim veniam, quis nostrud exercitation ullamco laboris nisi ut aliquip ex ea commodo consequat.</p>
  <span class="social s1" aria-hidden="true"></span>
  <span class="social s2" aria-hidden="true"></span>
  <span class="social s3" aria-hidden="true"></span>
</section>

</body>
</html>
```